Spring Football Signups

We need a flyer for spring football signups that highlights the team (Pellham Stormfoxes), the registration, schedules, the information regarding the different opportunities, and the About Us details of the Football Association.

Target Market(s)

Parents of Youth

Requirements
Must have
• Logos and team colors: purple and black

```html
<!DOCTYPE html>
<html lang="en">
<head>
<meta charset="utf-8">
<title>Pellham Stormfoxes – 2012 Sign-Up Info</title>
<link href="https://fonts.googleapis.com/css2?family=Anton&family=Graduate&family=Pirata+One&family=Ubuntu:wght@700&family=Jost:wght@600&family=Oswald:wght@300;500;600&family=Noto+Sans:wght@400;700&display=swap" rel="stylesheet">
<style>
  :root{
    --purple:#5b2679;
    --purple-dark:#2e0f40;
    --ink:#111111;
    --band:#d9d9d9;
    --shadow:#8c8c8c;
    --footer:#555555;
    --paper:#ffffff;
    --art-top:#4a2a62;
    --art-bottom:#141018;
    --cheer-top:#3a3a3a;
    --cheer-bottom:#0d0d0d;
  }
  *{margin:0;padding:0;box-sizing:border-box}
  html,body{width:927px;height:1200px;overflow:hidden;background:var(--paper)}
  .flyer{position:relative;width:927px;height:1200px;overflow:hidden;background:var(--paper);color:var(--ink)}

  .header-band{position:absolute;left:0;top:93px;width:927px;height:87px;background:var(--band)}

  .side-title{
    position:absolute;left:-518px;top:527px;width:1200px;height:140px;
    transform:rotate(-90deg);
    font-family:"Anton",sans-serif;font-size:134px;line-height:140px;
    text-align:center;letter-spacing:12px;color:var(--ink);
    text-shadow:9px 6px 7px var(--shadow);white-space:nowrap;
  }

  .team-city{
    position:absolute;left:200px;top:0;width:680px;text-align:center;
    font-family:"Graduate",serif;font-size:116px;line-height:120px;
    color:var(--purple);-webkit-text-stroke:2px var(--purple-dark);letter-spacing:1px;
    white-space:nowrap;
  }
  .team-name{
    position:absolute;left:180px;top:96px;width:720px;text-align:center;
    font-family:"Pirata One",cursive;font-size:86px;line-height:86px;
    color:var(--ink);letter-spacing:22px;padding-left:22px;white-space:nowrap;
  }

  .website{
    position:absolute;left:180px;top:188px;width:730px;text-align:center;
    font-family:"Ubuntu",sans-serif;font-weight:700;font-size:21px;color:var(--purple);
  }
  .venue{
    position:absolute;left:170px;top:230px;width:750px;text-align:center;
    font-family:"Jost",sans-serif;font-weight:600;font-size:21px;line-height:27px;color:var(--ink);
  }

  .program-mark{position:absolute}
  .association-mark{
    left:190px;top:345px;width:240px;height:185px;
    display:flex;flex-direction:column;align-items:center;justify-content:center;gap:14px;
    font-family:"Oswald",sans-serif;font-weight:600;font-size:24px;line-height:30px;
    color:var(--purple);text-align:center;
  }
  .association-mark .mark-square{width:46px;height:46px;background:var(--purple)}
  .hawk-art{
    left:214px;top:585px;width:216px;height:255px;border-radius:6px;
    background:linear-gradient(160deg,var(--art-top) 0%,var(--art-bottom) 100%);
  }
  .cheer-art{
    left:232px;top:904px;width:139px;height:216px;border-radius:6px;
    background:linear-gradient(180deg,var(--cheer-top) 0%,var(--cheer-bottom) 100%);
  }

  .program{position:absolute;left:430px;width:480px;text-align:center;color:var(--ink)}
  .program h2{
    font-family:"Oswald",sans-serif;font-weight:500;font-size:21px;color:var(--purple);
    letter-spacing:.3px;margin-bottom:10px;
  }
  .program p{font-family:"Oswald",sans-serif;font-weight:300;font-size:16.5px;line-height:22px;margin-bottom:12px}
  .program .tight{line-height:17px}
  .program .divisions{line-height:17px}
  .flag{top:337px}
  .tackle{top:627px}
  .cheer{top:908px}
  .cheer h2{font-family:"Noto Sans",sans-serif;font-weight:700;font-size:21px}
  .cheer p{font-family:"Noto Sans",sans-serif;font-weight:400;font-size:16.5px;line-height:23px;margin-bottom:10px}

  .footer{
    position:absolute;left:30px;top:1160px;width:880px;text-align:center;
    font-family:"Noto Sans",sans-serif;font-size:15.5px;line-height:20px;
    letter-spacing:2.6px;color:var(--footer);white-space:nowrap;
  }
</style>
</head>
<body>
<main class="flyer">
  <div class="header-band"></div>
  <div class="side-title">2012 SIGN-UP INFO</div>

  <h1>
    <span class="team-city">PELLHAM</span>
    <span class="team-name">STORMFOXES</span>
  </h1>

  <p class="website">For More Information Visit Our Website - www.pellhamfootball.org</p>
  <p class="venue">Hollister’s Market Parking Lot, 418 W. Oak Avenue, Pellham, Texas 75990<br>Saturdays, 10:00am – 2:00pm</p>

  <div class="program-mark association-mark">
    <span class="mark-square"></span>
    <span>Pellham Independent<br>Football Association</span>
  </div>

  <section class="program flag">
    <h2>YOUTH FLAG FOOTBALL</h2>
    <p class="tight">PIFA offers a Flag Football Program for children in Kindergarten<br>&amp; Pre-K.</p>
    <p>Flag football is utilized primarily to provide an opportunity to partici-<br>pate and learn the basics of playing football.</p>
    <p>Sign-Up Fees are $50 per player. Each player will be provided a<br>Jersey, Flag Belts, CPFA League Registration and Insurance.</p>
  </section>

  <div class="program-mark hawk-art" role="img" aria-label="Illustration of a diving hawk with spread wings in black and purple"></div>

  <section class="program tackle">
    <h2>YOUTH TACKLE FOOTBALL</h2>
    <p>Pellham Independent Football offers (3) Divisions for Tackle Football:</p>
    <p class="divisions">Bantam Division – Grades 1 &amp; 2<br>Minor Division – Grades 3 &amp; 4<br>Major Division – Grades 5 &amp; 6</p>
    <p>Sign-Up Fees are $150 per player. Each player will beprovided a<br>Jersey, Football Pants, CPFA League Registration and Insurance.</p>
  </section>

  <div class="program-mark cheer-art" role="img" aria-label="Black silhouette of a cheerleader holding pom-poms overhead"></div>

  <section class="program cheer">
    <h2>YOUTH CHEERLEADING</h2>
    <p>PIFA offers an All Ages Welcome Cheerleading Program!!</p>
    <p>Anyone interested in cheerleading can participate and<br>cheer for teams in any division.</p>
    <p>Sign-Ups Fees are $250. Cheerleaders are provided with<br>full cheer uniform and pom-poms.</p>
  </section>

  <footer class="footer">
    P. I. F. A.&nbsp; is a proud member of Cedar Plains Football&nbsp; Association<br>
    Pellham Independent Football&nbsp; Association - PO Box 384 - Pellham,&nbsp; Texas 75990
  </footer>
</main>
</body>
</html>
```